https://dorvakel.com

We need a cool technology design for our Managed IT Services company. We are located in Coral Springs Florida. We provide all IT services and support for small to medium sized businesses. We would like to see designs that use our blue and white colors from our website.

```html
<!DOCTYPE html>
<html lang="en">
<head>
<meta charset="UTF-8">
<title>Dorvakel Business Card</title>
<link href="https://fonts.googleapis.com/css2?family=Lato:wght@400;700;900&display=swap" rel="stylesheet">
<style>
  :root {
    --navy: #22345a;
    --sky: #5b86c4;
    --white: #ffffff;
    --mist: #d5d9df;
    --ink: #2a3550;
    --muted: #8a93a3;
    --stage: #5f6165;
  }
  * { margin: 0; padding: 0; box-sizing: border-box; }
  html, body { width: 1200px; height: 900px; overflow: hidden; }
  body {
    background: var(--stage);
    font-family: "Lato", sans-serif;
    display: flex;
    flex-direction: column;
    align-items: center;
    justify-content: center;
    gap: 48px;
  }
  .card {
    position: relative;
    width: 640px;
    height: 366px;
    border-radius: 22px;
    overflow: hidden;
    box-shadow: 0 14px 30px rgba(0,0,0,0.35);
  }

  /* Back side */
  .card-back { background: var(--navy); }
  .card-back .rule {
    position: absolute; left: 0; top: 212px;
    width: 380px; height: 7px; background: var(--white);
  }
  .card-back .wordmark {
    position: absolute; left: 200px; top: 120px;
    font-weight: 900; font-size: 72px; letter-spacing: 1px;
    color: var(--white); line-height: 1;
  }
  .card-back .site {
    position: absolute; left: 388px; top: 238px;
    font-size: 18px; letter-spacing: 5px; color: var(--white);
  }
  .card-back .accent {
    position: absolute; right: 0; top: 290px;
    width: 60px; height: 14px; background: var(--sky);
  }

  /* Front side */
  .card-front { background: var(--white); color: var(--ink); }
  .card-front .person { position: absolute; left: 40px; top: 34px; }
  .person .name { font-weight: 900; font-size: 19px; color: var(--navy); }
  .person .title { font-size: 13px; letter-spacing: 1px; color: var(--muted); }
  .card-front .wordmark {
    position: absolute; right: 44px; top: 72px;
    font-weight: 900; font-size: 50px; color: var(--navy); line-height: 1;
  }
  .card-front .band {
    position: absolute; left: 0; top: 148px; width: 100%; height: 118px;
    background: var(--navy);
    display: flex; justify-content: space-around; align-items: center;
    padding: 0 20px;
  }
  .contact { display: flex; flex-direction: column; align-items: center; gap: 8px;
    color: var(--white); font-size: 15px; }
  .contact svg { width: 16px; height: 16px; fill: none; stroke: var(--white); stroke-width: 1.8; }
  .card-front .address-strip {
    position: absolute; left: 0; top: 266px; width: 100%; height: 40px;
  }
  .address-strip .address {
    position: absolute; left: 104px; top: 0; height: 40px;
    display: flex; align-items: center; gap: 8px;
    font-size: 15px; color: var(--ink);
  }
  .address svg { width: 14px; height: 16px; fill: var(--navy); }
</style>
</head>
<body>

  <section class="card card-back">
    <div class="wordmark">DORVAKEL</div>
    <div class="rule"></div>
    <div class="site">dorvakel.com</div>
    <div class="accent"></div>
  </section>

  <section class="card card-front">
    <div class="person">
      <div class="name">YOUR NAME</div>
      <div class="title">JOB TITLE</div>
    </div>
    <div class="wordmark">DORVAKEL</div>

    <div class="band">
      <div class="contact">
        <svg viewBox="0 0 24 24"><path d="M5 3h4l2 5-3 2a11 11 0 0 0 6 6l2-3 5 2v4a2 2 0 0 1-2 2A17 17 0 0 1 3 5a2 2 0 0 1 2-2z"/></svg>
        <span>(555) 214-6089</span>
      </div>
      <div class="contact">
        <svg viewBox="0 0 24 24"><rect x="3" y="4" width="18" height="12" rx="1"/><path d="M9 20h6M12 16v4"/></svg>
        <span>dorvakel.com</span>
      </div>
      <div class="contact">
        <svg viewBox="0 0 24 24"><rect x="3" y="5" width="18" height="14" rx="1"/><path d="M3 6l9 7 9-7"/></svg>
        <span>youremail@example.com</span>
      </div>
    </div>

    <div class="address-strip">
      <svg width="640" height="40" viewBox="0 0 640 40" aria-hidden="true">
        <polygon points="64,0 640,0 640,40 84,40 84,16" fill="#d5d9df"/>
      </svg>
      <div class="address">
        <svg viewBox="0 0 14 18"><path d="M7 0a7 7 0 0 0-7 7c0 5 7 11 7 11s7-6 7-11a7 7 0 0 0-7-7zm0 10a3 3 0 1 1 0-6 3 3 0 0 1 0 6z"/></svg>
        <span>1820 Palm Crest Ave #140, Brightwater, Lakeshire 10293</span>
      </div>
    </div>
  </section>

</body>
</html>
```